Bref créative |
Harbourlea Dental Clinic | ||
business cards, letterhead and envelopes design | ||
Use same font as used in my logo | ||
Cutting-Edge Corporate Traditional Modern Professional Simple Bright & Fun-filled |
Dr. Kelsi Tomberg Ravinder | ||
Corrow Arcade - Shop 4.3C, 27 Fenwick Lane, Meadowbank, NSW 2114 |
kelsi@HarbourleaDentalClinic.com.au | ||
www.HarbourleaDentalClinic.com.au | ||
For Business Cards Please include: After-hours Emergency Service: Phone: 02 5173 6648 Mobile: 04 7825 1943 For Envelops Please include: Logo If not delivered please return to Corrow Arcade - Shop 4.3C, 27 Fenwick Lane, Meadowbank, NSW 2114 |
Appointment: For - Date - Time - If you are unable to keep your appointment, please contact us as soon as possible. |

```html
<!DOCTYPE html>
<html lang="en">
<head>
<meta charset="utf-8">
<title>Harbourlea Dental Clinic — Stationery</title>
<link href="https://fonts.googleapis.com/css2?family=Open+Sans:wght@400;600;700&display=swap" rel="stylesheet">
<style>
:root{
  --bg:#2b2b2d;
  --paper:#ffffff;
  --blue:#1f8fd1;
  --blue-dark:#0b5d9c;
  --blue-light:#63c6ef;
  --ink:#3d4850;
  --ink-soft:#8a949b;
  --rule:#c9d0d5;
  --band:linear-gradient(90deg,var(--blue-light),var(--blue) 50%,var(--blue-dark));
}
*{box-sizing:border-box;margin:0;padding:0}
html,body{width:1200px;height:614px;overflow:hidden;background:var(--bg);font-family:"Open Sans",Arial,sans-serif;color:var(--ink)}
.canvas{position:relative;width:1200px;height:614px}
.sheet{position:absolute;background:var(--paper);overflow:hidden;box-shadow:0 2px 6px rgba(0,0,0,.45)}
.brand{display:flex;align-items:center;gap:4px;font-weight:700;color:var(--blue);white-space:nowrap}
.brand-dot{width:9px;height:9px;border-radius:50%;background:var(--blue);flex:none}
.band{position:absolute;left:0;bottom:0;width:100%;background:var(--band)}
.tiny{font-size:4px;line-height:1.45;color:var(--ink-soft)}
.footer-url{position:absolute;bottom:8px;width:100%;text-align:center;font-size:4px;color:#fff}

/* letterheads */
.letterhead{top:139px;width:324px;height:437px}
.letterhead.fax{left:48px}
.letterhead.plain{left:413px}
.letterhead .brand{position:absolute;top:22px;left:18px;font-size:8px}
.letterhead .address{position:absolute;top:22px;left:150px;width:150px}
.letterhead .band{height:44px}
.fax-title{position:absolute;top:74px;left:18px;width:288px;text-align:center;font-size:6px;font-weight:700;letter-spacing:.5px}
.fax-table{position:absolute;top:84px;left:18px;width:288px;border-collapse:collapse;font-size:4px}
.fax-table td{border:.5px solid var(--rule);height:8px;padding:0 3px;width:25%}
.fax-table .label{font-weight:600}
.fax-message{position:absolute;top:142px;left:18px;width:288px;height:220px;border:.5px solid var(--rule);font-size:4px;font-weight:600;padding:3px}

/* compliment banner */
.banner{left:437px;top:53px;width:326px;height:62px;display:flex}
.banner .brand{font-size:7px;padding-left:10px;width:110px}
.banner-panel{flex:1;background:var(--band);color:#fff;padding:9px 12px;clip-path:polygon(8% 0,100% 0,100% 100%,0 100%)}
.banner-panel h1{font-size:10px;font-weight:600;white-space:nowrap}
.banner-panel p{font-size:4px;line-height:1.5;opacity:.9}

/* business cards */
.card{top:182px;width:113px;height:56px}
.card.front{left:775px;background:linear-gradient(90deg,var(--paper) 35%,var(--blue-light) 36%,var(--blue) 70%,var(--blue-dark))}
.card.back{left:900px}
.card.front .info{position:absolute;left:44px;top:10px;color:#fff}
.card.front h2{font-size:5px;font-weight:700;white-space:nowrap}
.card.front p{font-size:3.2px;line-height:1.5}
.card.back .brand{position:absolute;left:8px;top:6px;font-size:5px}
.card.back .brand-dot{width:5px;height:5px}
.appointment{position:absolute;left:8px;top:15px;width:98px;font-size:3.2px;line-height:1.5;color:var(--ink)}
.appointment h3{font-size:4px;font-weight:700;color:var(--blue)}
.appointment .field{display:flex;gap:2px}
.appointment .field span{flex:1;border-bottom:.4px solid var(--rule)}
.appointment .note{color:var(--ink-soft);margin-top:1px}
.card.back .band{height:4px}

/* envelopes */
.envelope{left:775px;width:377px}
.envelope.front{top:362px;height:125px}
.envelope.front .brand{position:absolute;left:16px;top:16px;font-size:7px}
.envelope.front .return{position:absolute;left:16px;top:34px;width:150px}
.envelope.front .band{height:26px}
.envelope.back{top:504px;height:82px}
.envelope.back .band{top:0;bottom:auto;height:56px}
.envelope.back .footer-url{bottom:auto;top:25px;font-size:5px}
</style>
</head>
<body>
<main class="canvas">

  <section class="sheet letterhead fax" aria-label="Fax cover letterhead">
    <div class="brand"><span class="brand-dot"></span>Harbourlea Dental Clinic</div>
    <p class="tiny address">Corrow Arcade - Shop 4.3C, 27 Fenwick Lane,<br>Meadowbank, NSW 2114<br>P: 02 5173 6648 &nbsp; M: 04 7825 1943<br>kelsi@HarbourleaDentalClinic.com.au</p>
    <h2 class="fax-title">FAX COVER</h2>
    <table class="fax-table">
      <tr><td class="label">TO:</td><td></td><td class="label">FROM:</td><td></td></tr>
      <tr><td class="label">COMPANY:</td><td></td><td class="label">DATE:</td><td></td></tr>
      <tr><td class="label">FAX:</td><td></td><td class="label">PAGES:</td><td></td></tr>
      <tr><td class="label">PHONE:</td><td></td><td class="label">URGENT:</td><td></td></tr>
      <tr><td class="label">RE:</td><td></td><td class="label">CC:</td><td></td></tr>
    </table>
    <div class="fax-message">MESSAGE:</div>
    <div class="band" role="img" aria-label="Blue wave footer graphic"></div>
    <p class="footer-url">www.HarbourleaDentalClinic.com.au</p>
  </section>

  <section class="sheet letterhead plain" aria-label="Letterhead">
    <div class="brand"><span class="brand-dot"></span>Harbourlea Dental Clinic</div>
    <p class="tiny address">Corrow Arcade - Shop 4.3C, 27 Fenwick Lane,<br>Meadowbank, NSW 2114<br>P: 02 5173 6648 &nbsp; M: 04 7825 1943<br>kelsi@HarbourleaDentalClinic.com.au</p>
    <div class="band" role="img" aria-label="Blue wave footer graphic"></div>
    <p class="footer-url">www.HarbourleaDentalClinic.com.au</p>
  </section>

  <section class="sheet banner" aria-label="Compliment slip">
    <div class="brand"><span class="brand-dot"></span>Harbourlea Dental Clinic</div>
    <div class="banner-panel">
      <h1>Dr. Kelsi Tomberg Ravinder</h1>
      <p>Corrow Arcade - Shop 4.3C, 27 Fenwick Lane, Meadowbank, NSW 2114<br>P: 02 5173 6648 &nbsp; M: 04 7825 1943<br>kelsi@HarbourleaDentalClinic.com.au</p>
    </div>
  </section>

  <section class="sheet card front" aria-label="Business card front">
    <div class="info">
      <h2>Dr. Kelsi Tomberg Ravinder</h2>
      <p>After-hours Emergency Service<br>Phone: 02 5173 6648<br>Mobile: 04 7825 1943<br>kelsi@HarbourleaDentalClinic.com.au</p>
    </div>
  </section>

  <section class="sheet card back" aria-label="Appointment card">
    <div class="brand"><span class="brand-dot"></span>Harbourlea Dental Clinic</div>
    <div class="appointment">
      <h3>Appointment</h3>
      <div class="field">For:<span></span></div>
      <div class="field">Date:<span></span>Time:<span></span></div>
      <p class="note">If you are unable to keep your appointment, please contact us as soon as possible.</p>
    </div>
    <div class="band" role="img" aria-label="Blue wave edge graphic"></div>
  </section>

  <section class="sheet envelope front" aria-label="Envelope front">
    <div class="brand"><span class="brand-dot"></span>Harbourlea Dental Clinic</div>
    <p class="tiny return">If not delivered please return to<br>Corrow Arcade - Shop 4.3C, 27 Fenwick Lane,<br>Meadowbank, NSW 2114</p>
    <div class="band" role="img" aria-label="Blue wave footer graphic"></div>
    <p class="footer-url">www.HarbourleaDentalClinic.com.au</p>
  </section>

  <section class="sheet envelope back" aria-label="Envelope back">
    <div class="band" role="img" aria-label="Blue wave flap graphic"></div>
    <p class="footer-url">www.HarbourleaDentalClinic.com.au</p>
  </section>

</main>
</body>
</html>
```